Weight Loss Challenge Social Media Graphics

Create 6-7 individual social media graphics (square size) to encourage folks to join our weight loss challenge. For the color scheme of the graphics, use the color palette attached

Note: each graphic can contain any of the stock photography attached or just the single picture of me (brown shirt) but a few should be ONLY the text
For some graphics we can say: JOIN US!
For some graphics, use only TEXT based

Target Market(s)

primarily women who want to get healthy

Industry/Entity Type

health and weight loss

Requirements
Must have
• The largest text should be: Ninety Days Bold

```html
<!DOCTYPE html>
<html lang="en">
<head>
<meta charset="utf-8">
<title>Lose Up to 20 Pounds – Challenge Graphic</title>
<link rel="stylesheet" href="https://fonts.googleapis.com/css2?family=Caprasimo&family=Playfair+Display:wght@400;700&display=swap">
<style>
  :root {
    --mauve: #9b7e7d;
    --blush: #fbd1e3;
    --sand: #ecd2c0;
    --cocoa: #4d4545;
  }
  html, body {
    margin: 0;
    padding: 0;
    width: 1200px;
    height: 1200px;
    overflow: hidden;
  }
  .post {
    position: relative;
    width: 1200px;
    height: 1200px;
    background: var(--sand);
    overflow: hidden;
  }
  .post__backdrop {
    position: absolute;
    inset: 0;
    width: 1200px;
    height: 1200px;
  }
  .backdrop__top { fill: var(--mauve); }
  .backdrop__bottom { fill: var(--sand); }
  .backdrop__bubble { fill: var(--blush); }

  .headline,
  .amount,
  .unit,
  .start-date {
    position: absolute;
    left: 0;
    width: 100%;
    margin: 0;
    text-align: center;
    white-space: nowrap;
  }
  .headline {
    top: 98px;
    font-family: "Caprasimo", "Cooper Black", serif;
    font-size: 104px;
    line-height: 1.2;
    color: var(--blush);
    letter-spacing: 1px;
  }
  .amount {
    top: 360px;
    font-family: "Playfair Display", "Bodoni Moda", serif;
    font-weight: 700;
    font-size: 300px;
    line-height: 1;
    color: var(--cocoa);
    letter-spacing: -4px;
  }
  .unit {
    top: 660px;
    font-family: "Playfair Display", serif;
    font-weight: 400;
    font-size: 112px;
    line-height: 1.1;
    color: var(--cocoa);
    letter-spacing: -2px;
  }
  .start-date {
    top: 965px;
    font-family: "Playfair Display", serif;
    font-weight: 400;
    font-size: 100px;
    line-height: 1.1;
    color: var(--cocoa);
    letter-spacing: -2px;
  }
  .start-date sup {
    font-size: 50px;
    vertical-align: 46px;
    line-height: 0;
  }
</style>
</head>
<body>
  <main class="post">
    <svg class="post__backdrop" viewBox="0 0 1200 1200" aria-hidden="true">
      <rect class="backdrop__top" x="0" y="0" width="1200" height="597"/>
      <rect class="backdrop__bottom" x="0" y="597" width="1200" height="603"/>
      <circle class="backdrop__bubble" cx="0" cy="597" r="324"/>
      <circle class="backdrop__bubble" cx="600" cy="597" r="324"/>
      <circle class="backdrop__bubble" cx="1200" cy="597" r="324"/>
    </svg>

    <h1 class="headline">Lose Up to</h1>
    <p class="amount">20</p>
    <p class="unit">Pounds</p>
    <p class="start-date">Begins Monday, Jan 6<sup>th</sup></p>
  </main>
</body>
</html>
```